Redesign of Wine Label

A redesign of a French wine label (attached below - Images 1-3) that changes the following elements:
- Change out the ducks on a bicycle for a man on an old-fashioned bicycle (such as a penny-farthing bicycle) wearing the traditional hat of Gascogne, France (please see the following link - https://www.picsharely.com/domaine_morvenol/ - where you can find many examples of the red hat referenced)
- Please rearrange the words "Domaine Morvenol" so that the word "Morvenol" is larger, about double the size of the word "Domaine"
- Please include the words "Les Cousins" somewhere around "Domaine Morvenol" in a manner that shows the connection.
- Please include the words "Côtes de Gascogne" somewhere in smaller, though clearly visible, letters closer to the bottom of the label.
- Please make the bicycle like the old image attached, with two aristocratic men in the same type of clothing riding it.

```html
<!DOCTYPE html>
<html lang="fr">
<head>
<meta charset="utf-8">
<title>Domaine Morvenol – Malbec labels</title>
<link rel="stylesheet" href="https://fonts.googleapis.com/css2?family=Cormorant+Garamond:wght@400;500&family=Montserrat:wght@300&family=Dancing+Script:wght@400&display=swap">
<style>
  :root {
    --page: #efeee9;
    --paper: #ffffff;
    --ink: #2b2b2b;
    --ink-soft: #4a4a4a;
    --ink-light: #6d6d6d;
    --art-red: #b3362b;
    --art-brown: #7a5a44;
    --art-beige: #e9e1d3;
  }
  * { margin: 0; padding: 0; box-sizing: border-box; }
  html, body {
    width: 1125px;
    height: 1200px;
    overflow: hidden;
    background: var(--page);
  }
  .sheet {
    position: relative;
    width: 1125px;
    height: 1200px;
    display: flex;
    justify-content: center;
    align-items: center;
    gap: 60px;
  }
  .label {
    position: relative;
    width: 470px;
    height: 505px;
    background: var(--paper);
    box-shadow: 0 2px 10px rgba(0,0,0,0.08);
    color: var(--ink);
    text-align: center;
  }
  .label__domaine {
    position: absolute;
    top: 22px; left: 0; right: 0;
    font-family: "Cormorant Garamond", serif;
    font-weight: 400;
    font-size: 30px;
    letter-spacing: 6px;
    color: var(--ink-soft);
  }
  .label__name {
    position: absolute;
    top: 52px; left: 0; right: 0;
    font-family: "Cormorant Garamond", serif;
    font-weight: 500;
    font-size: 84px;
    line-height: 1;
    letter-spacing: 1px;
    color: var(--ink);
  }
  .label__art {
    position: absolute;
    top: 148px; left: 98px;
    width: 272px;
    height: 262px;
    display: block;
  }
  .label__cousins {
    position: absolute;
    top: 176px; left: 314px;
    font-family: "Dancing Script", cursive;
    font-size: 16px;
    color: var(--ink-soft);
  }
  .label__variety {
    position: absolute;
    top: 408px; left: 0; right: 0;
    font-family: "Cormorant Garamond", serif;
    font-size: 30px;
    letter-spacing: 6px;
    color: var(--ink-soft);
  }
  .label__appellation {
    position: absolute;
    top: 446px; left: 0; right: 0;
    font-family: "Cormorant Garamond", serif;
    font-weight: 500;
    font-size: 24px;
    color: var(--ink);
  }
  .label__bottled {
    position: absolute;
    top: 478px; left: 0; right: 0;
    font-family: "Montserrat", sans-serif;
    font-weight: 300;
    font-size: 14px;
    letter-spacing: 1px;
    color: var(--ink-light);
  }
</style>
</head>
<body>
<main class="sheet">
  <section class="label">
    <p class="label__domaine">DOMAINE</p>
    <h1 class="label__name">MORVENOL</h1>
    <svg class="label__art" viewBox="0 0 272 262" role="img" aria-label="Illustration: two cousins in red Gascon berets and vintage suits riding a tandem bicycle with a basket">
      <defs>
        <linearGradient id="artToneA" x1="0" y1="0" x2="0" y2="1">
          <stop offset="0" stop-color="var(--art-red)" stop-opacity="0.35"/>
          <stop offset="0.5" stop-color="var(--art-beige)"/>
          <stop offset="1" stop-color="var(--art-brown)" stop-opacity="0.35"/>
        </linearGradient>
      </defs>
      <rect width="272" height="262" rx="6" fill="url(#artToneA)"/>
    </svg>
    <p class="label__cousins">Les Cousins</p>
    <p class="label__variety">MALBEC</p>
    <p class="label__appellation">CÔTES DE GASCOGNE</p>
    <p class="label__bottled">MIS EN BOUTEILLE À LA PROPRIÉTÉ</p>
  </section>

  <section class="label">
    <p class="label__domaine">DOMAINE</p>
    <h1 class="label__name">MORVENOL</h1>
    <svg class="label__art" viewBox="0 0 272 262" role="img" aria-label="Illustration: two cheerful cousins in red berets and dark jackets on a tandem bicycle, one waving a French flag">
      <defs>
        <linearGradient id="artToneB" x1="0" y1="0" x2="0" y2="1">
          <stop offset="0" stop-color="var(--art-red)" stop-opacity="0.4"/>
          <stop offset="0.5" stop-color="#4a4a55" stop-opacity="0.3"/>
          <stop offset="1" stop-color="var(--art-brown)" stop-opacity="0.35"/>
        </linearGradient>
      </defs>
      <rect width="272" height="262" rx="6" fill="url(#artToneB)"/>
    </svg>
    <p class="label__cousins">Les Cousins</p>
    <p class="label__variety">MALBEC</p>
    <p class="label__appellation">CÔTES DE GASCOGNE</p>
    <p class="label__bottled">MIS EN BOUTEILLE À LA PROPRIÉTÉ</p>
  </section>
</main>
</body>
</html>
```